Meadowlark Counseling Partners, LLC Needs Modern Business Card Design.

We provide behavioral health services from western Kansas to eastern Kansas. There is an abundance of competition for the services we provide with our main competitor being larger and having significantly more financial resources; however, the quality of services we provide is greater and we have started to catch the attention of the State of Kansas. We had a great logo designed by ArtFolio - this will be used to build upon our brand. The logo (attached) should be used in the card development. We want something unique, modern, but also a card design that clearly states our name, contact info, provides the name and unqiue location of each clinician, etc. Rounded edges, or a unique size, just something that makes our business card stand out from others. I have also uploaded each clinician's name and their unique location and phone number.

Our idea is to have one side be black with our logo. Then, on the other side have business cards for each individual. Plus, we want one card that is "generic" with no specific clinician's name listed so that we can give clients an appointment card when they leave. Some clinicians have two locations - we're open to design and background color, but we have started going with branding colors of black, the yellow in the logo files attached, and sometimes a gray. Our new office has been decorated using this theme.

Target Market(s)

individuals and families in need of behavioral health services; potential professional referral sources; existing referral sources

Industry/Entity Type

Business

Contact Information for Business Card

I attached a Word doc that provides clinician names, credentials and location information specific to each individual.

Font styles to use
Serif

Colors
000000
fbed22
dbdbdb
9d9d9d
c3c3c3

Requirements
Must have
• 1) use of the company logo that has been attached; 2) a template that provides us space to individualize business cards for all of our clinicians; 3) should stick to the colors we are branding with: black, yellow from the logo file, maybe a gray shade and we're open to a suggestion on a shade of white.
Nice to have
• Group discussion culminated in the thought that one side would be black with just our logo - no clinician names, etc. A unique design - rounded edges, unique size, some catchy lay-out would be nice.
Should not have
• Must not be too busy. Should look "clean." The project should stick to branding colors: black, yellow (from the logo file), maybe a gray and shade of white.

```html
<!DOCTYPE html>
<html lang="en">
<head>
<meta charset="utf-8">
<title>Meadowlark Counseling Partners – Business Card</title>
<link rel="stylesheet" href="https://fonts.googleapis.com/css2?family=Open+Sans:wght@400;600;700&display=swap">
<style>
  :root {
    --stage: #000000;
    --card-dark: #333335;
    --card-light: #ffffff;
    --brand-yellow: #fbc71c;
    --text-light: #f2f2f2;
    --text-dark: #1a1a1a;
    --divider: #5a5a5c;
  }
  * { margin: 0; padding: 0; box-sizing: border-box; }
  html, body {
    width: 1200px; height: 900px; overflow: hidden;
    background: var(--stage);
    font-family: "Open Sans", Arial, sans-serif;
  }
  .card {
    position: absolute;
    top: 271px;
    width: 457px; height: 281px;
    border-radius: 14px;
  }
  .card--front { left: 137px; background: var(--card-dark); }
  .card--back { left: 626px; background: var(--card-light); overflow: hidden; }

  .brand-name {
    position: absolute;
    left: 20px; top: 150px;
    width: 228px;
    text-align: center;
    color: var(--brand-yellow);
    font-weight: 600;
    font-size: 15px;
    line-height: 20px;
    letter-spacing: 0.5px;
  }
  .front-divider {
    position: absolute;
    left: 244px; top: 70px;
    width: 1px; height: 150px;
    background: var(--divider);
  }
  .contact {
    position: absolute;
    left: 269px; top: 48px;
    color: var(--text-light);
    font-size: 12.5px;
    line-height: 19.5px;
  }
  .contact__name {
    color: var(--brand-yellow);
    font-weight: 700;
    font-size: 17px;
    line-height: 22px;
  }
  .contact__title { margin-bottom: 18px; }
  .contact__office { margin-bottom: 17px; }
  .contact__phone { display: flex; align-items: center; gap: 7px; }
  .contact__phone svg { width: 9px; height: 9px; fill: var(--brand-yellow); }

  .back-brand {
    position: absolute;
    left: 0; top: 48px; width: 100%;
    text-align: center;
    color: var(--brand-yellow);
    font-weight: 600;
    font-size: 20px;
    letter-spacing: 1px;
  }
  .appointment {
    position: absolute;
    left: 0; top: 137px; width: 100%;
    text-align: center;
    color: var(--text-dark);
    font-size: 12.5px;
    line-height: 31px;
  }
  .appointment__company { font-weight: 700; }
  .tagline {
    position: absolute;
    left: 0; top: 240px; width: 100%;
    display: flex; align-items: center; gap: 10px;
    color: var(--text-dark);
    font-weight: 700;
    font-size: 16.5px;
    white-space: nowrap;
  }
  .tagline::before, .tagline::after {
    content: ""; flex: 1; height: 1.5px; background: var(--brand-yellow);
  }
</style>
</head>
<body>
  <section class="card card--front">
    <p class="brand-name">Meadowlark Counseling<br>Partners, LLC</p>
    <div class="front-divider"></div>
    <div class="contact">
      <p class="contact__name">Daniel R. Hollis, LP</p>
      <p class="contact__title">President</p>
      <div class="contact__office">
        <p>418 S. Willow Ave.</p>
        <p>Westbrook, Kansas 67100</p>
        <p class="contact__phone"><svg viewBox="0 0 10 10"><path d="M2 0.5 L3.6 2.6 L2.7 3.6 Q3.6 5.6 6.4 7.3 L7.4 6.4 L9.5 8 L8.2 9.6 Q4.5 9.2 0.5 1.8 Z"/></svg>(316) 555-0142</p>
      </div>
      <div class="contact__office">
        <p>207 N. 12th St., Ste. 105</p>
        <p>Eastfield, Kansas 67300</p>
        <p class="contact__phone"><svg viewBox="0 0 10 10"><path d="M2 0.5 L3.6 2.6 L2.7 3.6 Q3.6 5.6 6.4 7.3 L7.4 6.4 L9.5 8 L8.2 9.6 Q4.5 9.2 0.5 1.8 Z"/></svg>(844) 555-0187</p>
      </div>
    </div>
  </section>

  <section class="card card--back">
    <p class="back-brand">Meadowlark Counseling Partners, LLC</p>
    <div class="appointment">
      <p class="appointment__company">Meadowlark Counseling Partners, LLC</p>
      <p>Your next appointment with ______________</p>
      <p>Has been scheduled for ___________________</p>
    </div>
    <p class="tagline">“Find your calm here.”</p>
  </section>
</body>
</html>
```